Packaging label for launch of sun dried tomato products.

Established family farm in South Africa growing fruit for the production of dried fruit. We need a packaging label for the launch of our sun dried tomato products ie dried tomatoes in olive oil, dried tomato flakes and tomato powder. Packaging will be a round glass "jam jar" and spice shaker bottle. Due to limited amount of product available we cannot market to the masses, but rather focus on conveying a message of quality and exclusivity.

Target Market(s)

Home chef

Industry/Entity Type

Food

Font styles to use
Serif

Requirements
Nice to have
• Include the farm name in the design. TAVSONE

```html
<!DOCTYPE html>
<html lang="en">
<head>
<meta charset="utf-8">
<title>Tavsone Sun-Dried Tomato Labels</title>
<link href="https://fonts.googleapis.com/css2?family=Oswald:wght@500;600;700&family=Montserrat:wght@400&display=swap" rel="stylesheet">
<style>
  :root {
    --page-bg: #f3f3f3;
    --label-red: #d42a1c;
    --label-red-deep: #b81e12;
    --band-green: #5aac3a;
    --title-yellow: #f6c21a;
    --title-white: #ffffff;
    --caption-grey: #a7a7a7;
    --tomato-light: #ee3b26;
    --tomato-dark: #a8140b;
  }
  html, body {
    margin: 0;
    padding: 0;
    width: 1200px;
    height: 2333px;
    overflow: hidden;
    background: var(--page-bg);
  }
  .sheet { position: relative; width: 1200px; height: 2333px; }
  .caption {
    position: absolute;
    left: 0;
    width: 1200px;
    text-align: center;
    font-family: "Montserrat", sans-serif;
    font-size: 25px;
    color: var(--caption-grey);
    margin: 0;
    line-height: 1;
  }
  .dimension {
    position: absolute;
    font-family: "Montserrat", sans-serif;
    font-size: 25px;
    color: var(--caption-grey);
    transform: translate(-50%, -50%) rotate(-90deg);
    white-space: nowrap;
  }
  .label {
    position: absolute;
    overflow: hidden;
    background: var(--label-red);
    font-family: "Oswald", sans-serif;
  }
  .label-band {
    position: absolute;
    left: 0; right: 0; bottom: 0;
    background: var(--band-green);
  }
  .tomato {
    position: absolute;
    border-radius: 50%;
    background: radial-gradient(circle at 40% 35%, var(--tomato-light), var(--label-red-deep) 70%, var(--tomato-dark));
    transform: translate(-50%, -50%);
  }
  .line {
    position: absolute;
    left: 0; right: 0;
    text-align: center;
    line-height: 1;
    transform: translateY(-50%);
    margin: 0;
    white-space: nowrap;
  }
  .brand-name { color: var(--title-white); font-weight: 700; letter-spacing: 2px; }
  .sub-title { color: var(--title-yellow); font-weight: 700; letter-spacing: 1px; }
  .main-title { color: var(--title-white); font-weight: 600; letter-spacing: -1px; }
  .accent-title { color: var(--title-yellow); font-weight: 500; letter-spacing: 1px; }
  .accent-title .dash { display: inline-block; width: 0.7em; height: 0.6em; vertical-align: middle; margin: 0 0.25em; }
  .claim {
    position: absolute;
    display: flex;
    align-items: center;
    gap: 6px;
    transform: translateY(-50%);
    margin: 0;
  }
  .claim-text {
    color: var(--title-white);
    font-weight: 600;
    line-height: 1.05;
    text-align: center;
  }
  .claim-icon { display: block; }

  /* Jar label */
  .label-jar { left: 166px; top: 1079px; width: 869px; height: 604px; }
  .label-jar .label-band { height: 120px; }
  .label-jar .brand-name { top: 81px; font-size: 96px; }
  .label-jar .sub-title { top: 202px; font-size: 68px; }
  .label-jar .main-title { top: 294px; font-size: 112px; }
  .label-jar .accent-title { top: 386px; font-size: 52px; }
  .label-jar .claim { top: 547px; }
  .label-jar .claim-text { font-size: 27px; }
  .label-jar .claim-icon { width: 54px; height: 60px; }

  /* Shaker label */
  .label-shaker { left: 305px; top: 1802px; width: 590px; height: 454px; }
  .label-shaker .label-band { height: 95px; }
  .label-shaker .brand-name { top: 64px; font-size: 72px; }
  .label-shaker .sub-title { top: 149px; font-size: 50px; }
  .label-shaker .main-title { top: 218px; font-size: 80px; }
  .label-shaker .accent-title { top: 297px; font-size: 64px; }
  .label-shaker .claim { top: 413px; gap: 3px; }
  .label-shaker .claim-text { font-size: 20px; }
  .label-shaker .claim-icon { width: 40px; height: 44px; }
</style>
</head>
<body>
<svg width="0" height="0" style="position:absolute">
  <defs>
    <symbol id="icon-leaf" viewBox="0 0 54 60">
      <g fill="none" stroke="#fff" stroke-width="3" stroke-linecap="round" stroke-linejoin="round">
        <path d="M30 56 C30 40 34 22 44 6 C52 20 46 36 30 44"/>
        <path d="M28 56 C24 46 16 38 4 36 C6 48 16 54 28 50"/>
      </g>
    </symbol>
    <symbol id="icon-wheat" viewBox="0 0 54 60">
      <g fill="none" stroke="#fff" stroke-width="3" stroke-linecap="round" stroke-linejoin="round">
        <path d="M6 56 L40 10"/>
        <path d="M40 10 C38 4 42 2 46 2 C46 8 44 10 40 10Z"/>
        <path d="M32 22 C26 20 24 14 26 10 C32 12 34 18 32 22Z"/>
        <path d="M32 22 C38 24 44 22 46 18 C40 16 34 18 32 22Z"/>
        <path d="M24 33 C18 31 16 25 18 21 C24 23 26 29 24 33Z"/>
        <path d="M24 33 C30 35 36 33 38 29 C32 27 26 29 24 33Z"/>
        <path d="M16 44 C10 42 8 36 10 32 C16 34 18 40 16 44Z"/>
        <path d="M16 44 C22 46 28 44 30 40 C24 38 18 40 16 44Z"/>
      </g>
    </symbol>
    <symbol id="dash-left" viewBox="0 0 40 34">
      <g stroke="#fff" stroke-width="5" stroke-linecap="round">
        <path d="M4 6 L34 12"/><path d="M8 19 L36 17"/><path d="M6 30 L30 24"/>
      </g>
    </symbol>
    <symbol id="dash-right" viewBox="0 0 40 34">
      <g stroke="#fff" stroke-width="5" stroke-linecap="round">
        <path d="M36 6 L8 14"/><path d="M4 19 L32 19"/><path d="M10 28 L36 30"/>
      </g>
    </symbol>
  </defs>
</svg>
<main class="sheet">

  <p class="caption" style="top:1020px;">Label / Dried tomatoes in oil / Front side</p>

  <section class="label label-jar">
    <div class="label-band"></div>
    <div class="tomato" style="left:137px;top:136px;width:190px;height:190px;" role="img" aria-label="Photo of a whole ripe tomato with green stem"></div>
    <div class="tomato" style="left:82px;top:400px;width:170px;height:170px;" role="img" aria-label="Photo of a whole ripe tomato with green stem"></div>
    <div class="tomato" style="left:742px;top:124px;width:190px;height:190px;" role="img" aria-label="Photo of a halved tomato showing seeds"></div>
    <div class="tomato" style="left:780px;top:341px;width:182px;height:182px;" role="img" aria-label="Photo of a whole ripe tomato with green stem"></div>
    <div class="tomato" style="left:312px;top:528px;width:200px;height:200px;" role="img" aria-label="Photo of a halved tomato showing seeds"></div>
    <div class="tomato" style="left:476px;top:530px;width:186px;height:186px;" role="img" aria-label="Photo of a whole ripe tomato with green stem"></div>
    <div class="tomato" style="left:616px;top:518px;width:130px;height:130px;" role="img" aria-label="Photo of a tomato wedge"></div>

    <p class="line brand-name">TAVSONE</p>
    <p class="line sub-title">SUN-DRIED</p>
    <h1 class="line main-title">TOMATOES</h1>
    <p class="line accent-title"><svg class="dash" aria-hidden="true"><use href="#dash-left"/></svg>WITH OIL OLIVE<svg class="dash" aria-hidden="true"><use href="#dash-right"/></svg></p>
    <p class="claim" style="left:48px;"><svg class="claim-icon" aria-hidden="true"><use href="#icon-leaf"/></svg><span class="claim-text">ALL<br>NATURAL</span></p>
    <p class="claim" style="left:692px;"><span class="claim-text">GLUTEN<br>FREE</span><svg class="claim-icon" aria-hidden="true"><use href="#icon-wheat"/></svg></p>
  </section>

  <span class="dimension" style="left:1083px;top:1381px;">H = 80 mm</span>

  <p class="caption" style="top:1749px;">Label / Dried tomato powder / Front side</p>

  <section class="label label-shaker">
    <div class="label-band"></div>
    <div class="tomato" style="left:60px;top:91px;width:140px;height:140px;" role="img" aria-label="Photo of a whole ripe tomato with green stem"></div>
    <div class="tomato" style="left:45px;top:304px;width:118px;height:118px;" role="img" aria-label="Photo of a whole ripe tomato with green stem"></div>
    <div class="tomato" style="left:522px;top:87px;width:140px;height:140px;" role="img" aria-label="Photo of a halved tomato showing seeds"></div>
    <div class="tomato" style="left:548px;top:260px;width:136px;height:136px;" role="img" aria-label="Photo of a whole ripe tomato"></div>
    <div class="tomato" style="left:200px;top:422px;width:140px;height:140px;" role="img" aria-label="Photo of a halved tomato showing seeds"></div>
    <div class="tomato" style="left:326px;top:418px;width:134px;height:134px;" role="img" aria-label="Photo of a whole ripe tomato with green stem"></div>
    <div class="tomato" style="left:432px;top:410px;width:96px;height:96px;" role="img" aria-label="Photo of a tomato wedge"></div>

    <p class="line brand-name">TAVSONE</p>
    <p class="line sub-title">SUN-DRIED</p>
    <h2 class="line main-title">TOMATO</h2>
    <p class="line accent-title"><svg class="dash" aria-hidden="true"><use href="#dash-left"/></svg>POWDER<svg class="dash" aria-hidden="true"><use href="#dash-right"/></svg></p>
    <p class="claim" style="left:8px;"><svg class="claim-icon" aria-hidden="true"><use href="#icon-leaf"/></svg><span class="claim-text">ALL<br>NATURAL</span></p>
    <p class="claim" style="left:486px;"><span class="claim-text">GLUTEN<br>FREE</span><svg class="claim-icon" aria-hidden="true"><use href="#icon-wheat"/></svg></p>
  </section>

  <span class="dimension" style="left:949px;top:2029px;">H = 60 mm</span>

</main>
</body>
</html>
```